Prepared Meal Delivery Website

Need a new modern design for a prepared meal delivery company that is hosted on Shopify.

Target Market(s)

Young Professionals

Industry/Entity Type

Prepared Meal Delivery Service

Number of Pages Required

5+ page

Requirements
Must have
• Use https://www.vorabelmeals.com/ as an example
Nice to have
• Vibrant page with call to action obvious and repeated
Should not have
• Generic look, grays/white/black

```html
<!DOCTYPE html>
<html lang="en">
<head>
<meta charset="utf-8">
<title>Swift Plate Meals</title>
<link href="https://fonts.googleapis.com/css2?family=Kanit:wght@400;500;600&family=Montserrat:wght@400;500;600;700&display=swap" rel="stylesheet">
<style>
:root{
  --green:#1fb673;
  --yellow:#ffd100;
  --yellow-dark:#e0a800;
  --wood:#1b1b1b;
  --ink:#1a1a1a;
  --white:#ffffff;
}
*{box-sizing:border-box;margin:0;padding:0}
html,body{width:1200px;height:4587px;overflow:hidden}
body{position:relative;font-family:"Montserrat",sans-serif;color:var(--ink);background:var(--white)}
section,footer{position:absolute;left:0;width:1200px;overflow:hidden}
.abs{position:absolute}
.heading{font-family:"Kanit",sans-serif;font-weight:500;text-transform:uppercase}
.btn{position:absolute;display:flex;align-items:center;justify-content:center;background:var(--yellow);border-radius:24px;font-family:"Kanit",sans-serif;font-weight:500;font-size:21px;color:var(--ink);box-shadow:0 4px 0 var(--yellow-dark)}
.photo{position:absolute}

/* hero */
.hero{top:0;height:694px;background:linear-gradient(90deg,#141414,#262626 40%,#1a1a1a)}
.hero-photo{left:560px;top:0;width:640px;height:694px;background:radial-gradient(ellipse at 55% 45%,#6f7a4a 0%,#5a4a34 40%,rgba(40,35,30,0) 70%),linear-gradient(160deg,rgba(30,30,30,0) 45%,#c9a21a 100%)}
.topbar-call{left:75px;top:14px;display:flex;gap:10px;color:var(--white);font-size:13px;line-height:14px}
.nav{left:74px;top:60px;width:1050px;height:38px;background:var(--green);border-radius:4px;color:var(--white);font-size:13px;font-weight:600}
.nav span{position:absolute;top:11px}
.brand-badge{left:542px;top:19px;width:120px;height:120px;border-radius:50%;background:var(--wood);border:4px solid var(--white);display:flex;align-items:center;justify-content:center;text-align:center;color:var(--white);font-family:"Kanit",sans-serif;font-size:15px;line-height:18px;font-weight:500}
.plan-top{left:952px;top:14px;width:171px;height:31px;background:var(--yellow);color:var(--ink);font-size:13px;font-weight:600;display:flex;align-items:center;justify-content:center;border-radius:2px}
.hero-kicker{left:116px;top:232px;color:#dcdcdc;font-family:"Kanit",sans-serif;font-size:21px}
.hero-title{left:114px;top:258px;color:var(--white);font-size:58px;line-height:62px;font-weight:600}
.hero-copy{left:118px;top:411px;width:410px;color:#e8e8e8;font-size:13px;line-height:20px}

/* about */
.about{top:694px;height:508px;background:var(--white)}
.about-ring{left:116px;top:121px;width:320px;height:320px;border-radius:50%;border:6px solid var(--ink)}
.about-name{left:116px;top:236px;width:320px;text-align:center;font-family:"Kanit",sans-serif;font-size:30px;line-height:44px;font-weight:500;letter-spacing:2px}
.about-title{left:598px;top:68px;font-size:31px}
.about-copy{left:598px;top:122px;width:535px;font-size:17px;line-height:30px}

/* how it works */
.how{top:1202px;height:680px;background:radial-gradient(ellipse at 50% 40%,#35302a,#151312 75%)}
.section-title{position:absolute;left:0;width:1200px;text-align:center;font-size:31px}
.step{position:absolute;top:151px;width:185px;height:365px;background:var(--green);border-radius:92px;text-align:center;color:var(--white)}
.step .photo{left:3px;top:3px;width:179px;height:179px;border-radius:50%;border:5px solid var(--yellow)}
.step h3{position:absolute;top:193px;width:100%;font-family:"Kanit",sans-serif;font-weight:500;color:var(--yellow);font-size:17px}
.step p{position:absolute;top:224px;left:20px;width:145px;font-size:12px;line-height:18px;font-weight:500}

/* gallery */
.gallery{top:1882px;height:611px;background:var(--white)}
.g{position:absolute;width:198px}

/* who */
.who{top:2493px;height:596px;background:radial-gradient(ellipse at 50% 50%,#1f2f3c,#101921 80%)}
.who-card{position:absolute;top:135px;width:221px;height:297px;background:var(--white);text-align:center}
.who-card .photo{left:12px;top:13px;width:197px;height:123px}
.who-card h3{position:absolute;top:157px;width:100%;font-family:"Kanit",sans-serif;font-weight:400;font-size:18px}
.who-card p{position:absolute;top:185px;left:18px;width:185px;font-size:11px;line-height:18.5px}

/* reviews */
.reviews{top:3089px;height:752px;background:linear-gradient(180deg,#c4c4c6,#d2d2d4 50%,#c2c2c4)}
.tab{position:absolute;top:140px;width:162px;height:48px;display:flex;align-items:center;justify-content:center;font-family:"Kanit",sans-serif;font-size:24px;border:2px solid var(--green)}
.video{left:267px;top:222px;width:666px;height:400px;border:12px solid var(--green);border-radius:10px;background:var(--green);box-shadow:0 6px 14px rgba(0,0,0,.3)}
.video .photo{left:0;top:0;width:642px;height:376px;background:linear-gradient(120deg,#3e4a3a,#8a8478 45%,#d9d6cf)}
.controls{left:20px;top:318px;width:602px;height:45px;background:#1d1d1d;border-radius:3px}
.dot{position:absolute;top:650px;width:24px;height:24px;border-radius:50%;background:#111;border:3px solid var(--green)}

/* join */
.join{top:3841px;height:392px;background:radial-gradient(ellipse at 50% 50%,#2e2b27,#121110 75%)}
.join-title{left:0;top:58px;width:1200px;text-align:center;color:var(--white);font-family:"Kanit",sans-serif;font-size:46px;font-weight:400}
.join-copy{left:0;top:139px;width:1200px;text-align:center;color:var(--white);font-size:20px;line-height:29px}

/* footer */
.footer{top:4233px;height:354px;background:linear-gradient(90deg,#191919,#262626 50%,#1a1a1a);border-top:3px solid #bdbdbd;color:var(--white)}
.foot-title{font-family:"Kanit",sans-serif;color:var(--yellow);font-size:17px;font-weight:500}
.foot-links{left:546px;top:80px;font-size:13px;font-weight:600;line-height:35.5px}
.contact{display:flex;gap:10px;font-size:13px;line-height:14px}
.icon-circle{width:30px;height:30px;border-radius:50%;border:2px solid var(--white);display:flex;align-items:center;justify-content:center}
.copyright{left:0;bottom:0;width:1200px;height:36px;background:#0d0d0d;text-align:center;font-size:12px;line-height:36px}
</style>
</head>
<body>

<section class="hero">
  <div class="photo hero-photo" role="img" aria-label="Food photo: plate of glazed salmon with spinach, edamame, corn, red cabbage and carrots on a wooden board over a yellow paint splash"></div>

  <div class="abs topbar-call">
    <svg width="30" height="30" viewBox="0 0 30 30" aria-hidden="true"><circle cx="15" cy="15" r="13.5" fill="none" stroke="#fff" stroke-width="2"/><path d="M10 8l3 0 1 4-2 1.5a9 9 0 0 0 4.5 4.5L18 16l4 1v3c0 1-1 2-2 2A12 12 0 0 1 8 10c0-1 1-2 2-2z" fill="#fff"/></svg>
    <div>CALL US<br>+1(555) 014 2290</div>
  </div>
  <svg class="abs" style="left:800px;top:18px" width="120" height="24" viewBox="0 0 120 24" aria-hidden="true">
    <circle cx="9" cy="9" r="6.5" fill="none" stroke="#fff" stroke-width="2.5"/><line x1="14" y1="14" x2="20" y2="20" stroke="#fff" stroke-width="2.5"/>
    <line x1="31" y1="2" x2="31" y2="22" stroke="#fff" stroke-width="1.5"/>
    <circle cx="60" cy="8" r="5" fill="#fff"/><path d="M50 21c0-6 4-8 10-8s10 2 10 8z" fill="#fff"/>
    <path d="M82 4h4l3 11h12l3-8H88" fill="none" stroke="#fff" stroke-width="2"/><circle cx="91" cy="19" r="2" fill="#fff"/><circle cx="100" cy="19" r="2" fill="#fff"/>
  </svg>
  <div class="abs plan-top">CHOOSE YOUR PLAN</div>
  <nav class="abs nav">
    <span style="left:76px">SHOP NOW</span>
    <span style="left:191px">BUSINESS PLAN</span>
    <span style="left:341px">GIFT CARDS</span>
    <span style="left:628px">REWARDS</span>
    <span style="left:736px">ABOUT US</span>
    <span style="left:847px">CONTACT US</span>
  </nav>
  <div class="abs brand-badge">SWIFT<br>PLATE<br>MEALS</div>

  <p class="abs hero-kicker">WELCOM TO OUR</p>
  <h1 class="abs heading hero-title">HEALTHY FOOD<br>COLLECTION!</h1>
  <p class="abs hero-copy">Lorem ipsum dolor sit amet, consectetur adipiscing elit, sed do eiusmod tempor incididunt ut labore et dolore magna aliqua. Quis ipsum suspendisse ultrices gravida.</p>
  <a class="btn" style="left:166px;top:513px;width:222px;height:43px">SHOP NOW</a>
</section>

<section class="about">
  <div class="abs about-ring"></div>
  <p class="abs about-name">SWIFT PLATE<br>MEALS</p>
  <div class="photo" role="img" aria-label="Bowl of sliced steak with greens and lime" style="left:351px;top:77px;width:160px;height:160px;border-radius:50%;border:5px solid #e8e8e8;background:radial-gradient(circle,#8a4a3a,#5f8a3a 55%,#d9d6cf 75%)"></div>
  <div class="photo" role="img" aria-label="Plate of stuffed peppers" style="left:18px;top:288px;width:178px;height:178px;border-radius:50%;border:5px solid #e8e8e8;background:radial-gradient(circle,#e0882a,#c9542a 45%,#e6e1d8 75%)"></div>
  <h2 class="abs heading about-title">ABOUT US</h2>
  <p class="abs about-copy">Let's be honest, it's not easy to eat healthily – it can take hours of planning, sourcing, cooking and cleaning to prepare a single nutritious and delicious meal (and that's assuming you can cook!). So with our increasingly busy lives, it's not surprising that fast food and unhealthy, processed, and packaged options easily become far too frequent occurrences. Fortunately,</p>
  <a class="btn" style="left:749px;top:385px;width:225px;height:46px">LEARN MORE</a>
</section>

<section class="how">
  <div class="photo" role="img" aria-label="Dark wooden table with raw steak, garlic, asparagus and spices" style="left:0;top:0;width:1200px;height:680px;background:radial-gradient(ellipse at 8% 20%,rgba(120,40,40,.35),transparent 30%),radial-gradient(ellipse at 92% 70%,rgba(80,110,50,.3),transparent 30%)"></div>
  <h2 class="heading section-title" style="top:66px;color:#fff">HOW IT WORKS</h2>
  <div class="step" style="left:214px">
    <div class="photo" role="img" aria-label="Laptop showing the meal plan menu" style="background:linear-gradient(140deg,#cfd8e6,#7d8ea8)"></div>
    <h3>CHOOSE A PLAN</h3>
    <p>Choose one of our pre-set plans, or Build Your Own!</p>
  </div>
  <div class="step" style="left:508px">
    <div class="photo" role="img" aria-label="Customer holding a meal delivery bag" style="background:linear-gradient(140deg,#e8e2da,#8c2f2f)"></div>
    <h3>AWAIT DELIVERY</h3>
    <p>We deliver twice weekly, on Sundays and Wednesdays Our delivery window is between 3pm and 8pm</p>
  </div>
  <div class="step" style="left:802px">
    <div class="photo" role="img" aria-label="Smiling athlete flexing" style="background:linear-gradient(140deg,#c7cbd2,#6d6a78)"></div>
    <h3>HEAT &amp; EAT</h3>
    <p>Place your meal in the microwave for 2-2.5 minutes or reheat to preferred temperature on a pan/skillet</p>
  </div>
  <a class="btn" style="left:457px;top:557px;width:285px;height:44px">CHOOSE YOUR PLAN</a>
</section>

<section class="gallery">
  <h2 class="heading section-title" style="top:68px">SPM FOOD GALLERY</h2>
  <div class="g photo" role="img" aria-label="Salmon with rice and greens" style="left:75px;top:131px;height:150px;background:linear-gradient(135deg,#d7b33a,#4f7d2e 60%,#e4e0d8)"></div>
  <div class="g photo" role="img" aria-label="Salmon bowl with vegetables" style="left:75px;top:297px;height:238px;background:radial-gradient(circle,#8a4d23,#5c8a2c 45%,#8c4d8f 60%,#ecebe6 75%)"></div>
  <div class="g photo" role="img" aria-label="Fresh salad containers" style="left:288px;top:131px;height:238px;background:linear-gradient(150deg,#6d9a3a,#a2457a 50%,#dcd8d0)"></div>
  <div class="g photo" role="img" aria-label="Noodles in a bowl with chopsticks" style="left:288px;top:385px;height:150px;background:linear-gradient(135deg,#c9a06a,#7a4a2c)"></div>
  <div class="g photo" role="img" aria-label="Shrimp with green beans and featured meal card" style="left:501px;top:131px;height:150px;background:linear-gradient(135deg,#e59a6a,#4b7d31 55%,#e9e4dc)"></div>
  <div class="g photo" role="img" aria-label="Meal prep containers with green beans" style="left:501px;top:297px;height:238px;background:linear-gradient(150deg,#e8e1cf,#5b8a35 50%,#d8cf9e)"></div>
  <div class="g photo" role="img" aria-label="Grain salad with carrots and cucumber" style="left:714px;top:131px;height:238px;background:linear-gradient(150deg,#8d8a6c,#6e9a3e 50%,#d77a2e)"></div>
  <div class="g photo" role="img" aria-label="Chicken with zucchini noodles" style="left:714px;top:385px;height:150px;background:linear-gradient(135deg,#c79552,#c8c078 55%,#ebe7df)"></div>
  <div class="g photo" role="img" aria-label="Beef with rice and broccoli" style="left:927px;top:131px;height:150px;background:linear-gradient(135deg,#6b4326,#c2a24a 50%,#4f7a2e)"></div>
  <div class="g photo" role="img" aria-label="Meal trays with salmon and sweet potato" style="left:927px;top:297px;height:238px;background:linear-gradient(150deg,#d97a4a,#6b8a3c 50%,#e9e3d8)"></div>
</section>

<section class="who">
  <div class="photo" role="img" aria-label="Dark table with peppers, cauliflower, potatoes and carrots" style="left:0;top:0;width:1200px;height:596px;background:radial-gradient(ellipse at 5% 40%,rgba(180,60,40,.35),transparent 25%),radial-gradient(ellipse at 95% 60%,rgba(200,110,40,.35),transparent 25%)"></div>
  <h2 class="heading section-title" style="top:62px;color:#fff">WHO IS SPM FOR ?</h2>
  <div class="who-card" style="left:215px">
    <div class="photo" role="img" aria-label="Healthcare worker holding a meal bag" style="background:linear-gradient(135deg,#d8cfbe,#2f5aa8)"></div>
    <h3>PROFESSIONAL</h3>
    <p>SPM is the ideal service for the professional on the go. We deliver twice weekly so you can focus on your career and prioritize your business without compromising on nutrition.</p>
  </div>
  <div class="who-card" style="left:490px">
    <div class="photo" role="img" aria-label="Family with their meal delivery" style="background:linear-gradient(135deg,#6a5a50,#d9d2c6)"></div>
    <h3>FAMILIES</h3>
    <p>Set your family up for success with a week of healthy meals planned ahead. By ordering the week before, you'll be able to serve your family healthy meals with minimal effort!</p>
  </div>
  <div class="who-card" style="left:762px">
    <div class="photo" role="img" aria-label="Person unpacking meals at home" style="background:linear-gradient(135deg,#e4e4e2,#9b9a98)"></div>
    <h3>SINGLES</h3>
    <p>Cooking can be tiring and costly for individuals. Enjoy a clean fridge full of as many or as few meals as you need! No more wasted ingredients, just pure sustainable joy of eating!</p>
  </div>
  <a class="btn" style="left:457px;top:473px;width:285px;height:44px">CHOOSE YOUR PLAN</a>
</section>

<section class="reviews">
  <h2 class="heading section-title" style="top:63px">WHAT OUR CUSTOMERS SAY ABOUT US</h2>
  <div class="tab" style="left:438px;background:var(--green);color:#fff">VIDEO</div>
  <div class="tab" style="left:603px;background:transparent">TEXT</div>
  <div class="abs video">
    <div class="photo" role="img" aria-label="Video testimonial of a customer speaking at home"></div>
    <div class="abs controls">
      <svg width="602" height="45" viewBox="0 0 602 45" aria-hidden="true">
        <rect x="14" y="11" width="7" height="23" fill="#fff"/><rect x="26" y="11" width="7" height="23" fill="#fff"/>
        <rect x="128" y="16" width="300" height="13" fill="#fff"/><rect x="130" y="18" width="230" height="9" fill="#555"/><rect x="130" y="18" width="36" height="9" fill="#1e8fe6"/>
        <rect x="452" y="27" width="3" height="6" fill="#1e8fe6"/><rect x="457" y="24" width="3" height="9" fill="#1e8fe6"/><rect x="462" y="21" width="3" height="12" fill="#1e8fe6"/><rect x="467" y="18" width="3" height="15" fill="#1e8fe6"/><rect x="472" y="14" width="3" height="19" fill="#1e8fe6"/>
        <circle cx="511" cy="22" r="8" fill="none" stroke="#fff" stroke-width="5" stroke-dasharray="3 2"/><circle cx="511" cy="22" r="3" fill="#1d1d1d"/>
        <path d="M546 12h7M546 12v7M570 12h-7M570 12v7M546 33h7M546 33v-7M570 33h-7M570 33v-7" stroke="#fff" stroke-width="3"/>
      </svg>
    </div>
  </div>
  <div class="dot" style="left:509px;background:var(--green)"></div>
  <div class="dot" style="left:549px"></div>
  <div class="dot" style="left:588px"></div>
  <div class="dot" style="left:625px"></div>
  <div class="dot" style="left:664px"></div>
</section>

<section class="join">
  <div class="photo" role="img" aria-label="Dark kitchen table with olive oil, spices and herbs" style="left:0;top:0;width:1200px;height:392px;background:radial-gradient(ellipse at 5% 20%,rgba(170,140,40,.3),transparent 25%),radial-gradient(ellipse at 95% 80%,rgba(90,120,50,.3),transparent 25%)"></div>
  <h2 class="abs join-title">JOIN THE <b style="font-weight:600">SPM</b> FAMILY!</h2>
  <p class="abs join-copy">Become a member and earn points &amp; exclusuve<br>rewards every time you order or refer a friend!</p>
  <a class="btn" style="left:367px;top:251px;width:222px;height:45px">JOIN NOW</a>
  <a class="btn" style="left:603px;top:251px;width:223px;height:45px">LOGIN</a>
</section>

<footer class="footer">
  <div class="abs" style="left:82px;top:33px;width:118px;height:118px;border-radius:50%;border:2px solid #fff;display:flex;align-items:center;justify-content:center;text-align:center;font-family:'Kanit',sans-serif;font-size:15px;line-height:18px;font-weight:500">SWIFT<br>PLATE<br>MEALS</div>
  <div class="abs contact" style="left:78px;top:175px">
    <div class="icon-circle"><svg width="16" height="16" viewBox="0 0 16 16" aria-hidden="true"><path d="M3 1h3l1 3.5-2 1.3a8 8 0 0 0 4.2 4.2L10.5 8 14 9v3c0 1-1 2-2 2A11 11 0 0 1 1 3c0-1 1-2 2-2z" fill="#fff"/></svg></div>
    <div>CALL US<br>+1(555) 014 2290</div>
  </div>
  <div class="abs contact" style="left:78px;top:229px">
    <div class="icon-circle"><svg width="16" height="12" viewBox="0 0 16 12" aria-hidden="true"><rect x="1" y="1" width="14" height="10" fill="none" stroke="#fff" stroke-width="1.5"/><path d="M1 1l7 6 7-6" fill="none" stroke="#fff" stroke-width="1.5"/></svg></div>
    <div>EMAIL<br>hello@swiftplatemeals.com</div>
  </div>
  <h3 class="abs foot-title" style="left:546px;top:30px">QUICK LINK</h3>
  <div class="abs foot-links">SHOP NOW<br>BUSINESS PLAN<br>GIFT CARDS<br>REWARDS<br>ABOUT US<br>CONTACT US</div>
  <h3 class="abs foot-title" style="left:860px;top:32px">WANT TO KEEP IN TOUCH!</h3>
  <div class="abs" style="left:860px;top:82px;width:263px;height:35px;border:3px solid var(--yellow);font-size:14px;line-height:29px;padding-left:10px">Enter email ID</div>
  <div class="abs" style="left:936px;top:137px;width:112px;height:35px;background:var(--green);font-size:14px;line-height:35px;text-align:center">SUBSCRIBE</div>
  <div class="abs" style="left:943px;top:210px;width:32px;height:32px;border-radius:50%;border:2px solid #fff"></div>
  <div class="abs" style="left:1002px;top:210px;width:32px;height:32px;border-radius:50%;border:2px solid #fff"></div>
  <p class="abs copyright">© 2022, Swift Plate Meals All Rights Reserved</p>
</footer>

</body>
</html>
```